Flyer Needed for Fun Choir Concert

8.5x11 flyer for upcoming choral concert. Theme is bluegrass/Americana. Need to incorporate preexisting logo. Pdf attached with copy and instructions.
Looking for flyer to communicate "bluegrass/Americana/fun"
Colors
Designer to choose colors to be used in the design.
Requirements
Must have
- Preexisting Solvarinette logo, photo of chorus, and photo of guest artists.

```html
<!DOCTYPE html>
<html lang="en">
<head>
<meta charset="utf-8">
<title>Roots and Wings – Solvarinette Concert Flyer</title>
<link href="https://fonts.googleapis.com/css2?family=Open+Sans:ital,wght@0,400;0,600;0,700;1,400&family=Roboto:wght@700&family=Cormorant+Garamond:ital,wght@1,700&family=Alfa+Slab+One&display=swap" rel="stylesheet">
<style>
  :root {
    --page-bg: #e9e4dc;
    --paper-light: #fffaea;
    --paper-mid: #f3e2b0;
    --paper-deep: #c9a25a;
    --brand-ink: #2c2a7a;
    --title-brown: #5a2410;
    --date-brown: #7a3a12;
    --ink: #2a2018;
    --diamond: #5a1c12;
    --photo-tone: #5f6a4e;
  }
  * { box-sizing: border-box; margin: 0; padding: 0; }
  html, body { width: 1200px; height: 1200px; overflow: hidden; }
  body { background: var(--page-bg); font-family: "Open Sans", sans-serif; color: var(--ink); position: relative; }

  .flyer {
    position: absolute; left: 215px; top: 30px; width: 770px; height: 1140px; overflow: hidden;
    background:
      radial-gradient(ellipse 70% 55% at 50% 52%, var(--paper-light) 0%, rgba(255,250,234,0.85) 45%, rgba(243,226,176,0) 80%),
      linear-gradient(180deg, var(--paper-deep) 0%, var(--paper-mid) 18%, var(--paper-light) 55%, var(--paper-mid) 85%, var(--paper-deep) 100%);
    box-shadow: 0 10px 30px rgba(0,0,0,0.25);
  }
  .flyer > * { position: absolute; }
  .center { left: 0; width: 100%; text-align: center; }

  .art-violin { left: 4px; top: 760px; width: 130px; height: 360px; border-radius: 65px 65px 55px 55px;
    background: linear-gradient(180deg, rgba(184,116,58,0.12), rgba(184,116,58,0.5)); }
  .art-guitar { left: 600px; top: 510px; width: 170px; height: 540px; border-radius: 40px 0 0 80px;
    background: linear-gradient(180deg, rgba(220,185,138,0.08) 0%, rgba(220,185,138,0.55) 55%, rgba(200,160,110,0.65) 100%); }

  .brand-name { top: 92px; font-size: 44px; font-weight: 600; color: var(--brand-ink); }
  .director { top: 172px; font-size: 17px; }
  .presents { top: 204px; font-size: 21px; font-style: italic; }

  .title { top: 250px; font-family: "Cormorant Garamond", serif; font-style: italic; font-weight: 700;
    font-size: 76px; line-height: 1; color: var(--title-brown); text-shadow: 1px 1px 0 #fff; }

  .dates { left: 86px; top: 355px; width: 598px; height: 46px; border: 1.5px solid var(--date-brown);
    font-family: "Roboto", sans-serif; font-weight: 700; font-size: 21px; color: var(--date-brown);
    display: flex; align-items: center; justify-content: center; gap: 14px; }
  .venue { top: 412px; font-size: 14.5px; letter-spacing: 0.3px; }

  .guest-photo { left: 86px; top: 463px; width: 368px; height: 220px;
    background: linear-gradient(160deg, #6f7a4f 0%, var(--photo-tone) 40%, #3c3a34 100%); }
  .blurb { left: 466px; top: 460px; width: 236px; text-align: center; font-size: 18.5px; line-height: 24.5px; }
  .blurb em { display: block; }

  .guests-intro { top: 698px; font-family: "Cormorant Garamond", serif; font-style: italic; font-weight: 700; font-size: 19px; }
  .guests { top: 733px; font-family: "Alfa Slab One", serif; font-size: 26px; color: var(--title-brown); letter-spacing: 0.5px; }
  .guests-desc { top: 772px; font-size: 18px; }
  .tickets-note { top: 818px; font-size: 16px; font-weight: 700; }

  .price { top: 852px; width: 128px; height: 128px; }
  .price text { font-family: "Open Sans", sans-serif; fill: #fff; text-anchor: middle; }
  .price .label { font-size: 13px; }
  .price .amount { font-size: 34px; font-weight: 700; }
  .price-general { left: 169px; }
  .price-seniors { left: 321px; }
  .price-students { left: 473px; }

  .childcare { top: 990px; font-size: 17px; }
  .website { top: 1022px; font-size: 19px; letter-spacing: 2.5px; }
</style>
</head>
<body>
  <main class="flyer">
    <div class="art-violin" role="img" aria-label="Illustration of a violin with bow"></div>
    <div class="art-guitar" role="img" aria-label="Illustration of an acoustic guitar"></div>

    <div class="brand-name center">Solvarinette</div>
    <div class="director center">Daniel Whitcombe, Artistic Director</div>
    <div class="presents center">presents</div>

    <h1 class="title center">Roots and Wings</h1>

    <div class="dates"><span>Saturday, May 5 at 7 pm</span><span>|</span><span>Sunday, May 6 at 3 pm</span></div>
    <div class="venue center">St. Aidan's Community Church &nbsp;| 1480 Juniper Street &nbsp;| &nbsp;Riverton</div>

    <div class="guest-photo" role="img" aria-label="Photo of the guest duo seated outdoors holding a violin and an acoustic guitar"></div>
    <p class="blurb">Join the singers of Solvarinette as we perform foot-tapping music with a distinctly American flavor, including Ellen Marrow's <em>"The Open Meadow: A Bluegrass Mass"!</em></p>

    <div class="guests-intro center">with special guests</div>
    <div class="guests center">MARISOL FENWICK &amp; THEO ARLUND</div>
    <div class="guests-desc center">purveyors of joyful acoustic Americana</div>
    <div class="tickets-note center">Tickets available online and at the door:</div>

    <svg class="price price-general" viewBox="0 0 128 128" aria-label="General admission $20">
      <rect x="22" y="22" width="84" height="84" rx="8" transform="rotate(45 64 64)" fill="var(--diamond)" stroke="#fff" stroke-width="3"/>
      <text class="label" x="64" y="50">General</text><text class="amount" x="64" y="86">$20</text>
    </svg>
    <svg class="price price-seniors" viewBox="0 0 128 128" aria-label="Seniors $15">
      <rect x="22" y="22" width="84" height="84" rx="8" transform="rotate(45 64 64)" fill="var(--diamond)" stroke="#fff" stroke-width="3"/>
      <text class="label" x="64" y="50">Seniors</text><text class="amount" x="64" y="86">$15</text>
    </svg>
    <svg class="price price-students" viewBox="0 0 128 128" aria-label="Students $10">
      <rect x="22" y="22" width="84" height="84" rx="8" transform="rotate(45 64 64)" fill="var(--diamond)" stroke="#fff" stroke-width="3"/>
      <text class="label" x="64" y="50">Students</text><text class="amount" x="64" y="86">$10</text>
    </svg>

    <div class="childcare center">Complimentary childcare provided at both performances.</div>
    <div class="website center">WWW.SOLVARINETTE-CHOIR.COM</div>
  </main>
</body>
</html>
```